Emerging jewellery maker and designer needs a business card design with logo

I need a business card to hand to industry officials and potential clients. I handmake my own jewellery that targets mostly females from 20 to 50 years of age. I use mostly sterling silver, with some gemstones and often have tribal or geometric elements in the design. The final design should communicate originality, simplicity and memorability.

Target Market(s)

20- 50 year old females

Industry/Entity Type

Business

Contact Information for Business Card

Title: Marisol Quenton Designs
Tagline: Jewellery and Object maker
Contact details:
-email: kmquenton4@mailvora.com
-instagram: @marisolquenton
-Mobile: 047-612-5093

Requirements
Must have
• Clear and strong design aesthetic
Nice to have
• I like symbols and use tribal and geometric symbols in my work. If this could be incorporated that would be great.( ideally a way better/digital version of the uploaded image could act as a logo of sorts)
Should not have
• Tacky sayings or quotes, misleading images, or an literal images of diamonds, rings etc

```html
<!DOCTYPE html>
<html lang="en">
<head>
<meta charset="UTF-8">
<title>Marisol Quenton Designs – Business Card</title>
<link rel="stylesheet" href="https://fonts.googleapis.com/css2?family=Open+Sans:wght@300;400&display=swap">
<style>
  :root {
    --page: #ffffff;
    --teal-light: #145a52;
    --teal-mid: #0d3f3a;
    --teal-dark: #06201d;
    --band: #0b0e0e;
    --ink: #f2f5f4;
    --ink-soft: #c9d3d1;
    --font-main: "Open Sans", sans-serif;
  }
  * { box-sizing: border-box; margin: 0; padding: 0; }
  html, body {
    width: 800px;
    height: 1200px;
    overflow: hidden;
    background: var(--page);
    font-family: var(--font-main);
  }
  .card {
    position: absolute;
    left: 78px;
    width: 700px;
    height: 460px;
    background: var(--band);
    overflow: hidden;
    color: var(--ink);
  }
  .card--front { top: 110px; }
  .card--back { top: 606px; }

  .card__texture {
    position: absolute;
    left: 0; top: 0;
    width: 100%;
    background:
      radial-gradient(ellipse at 50% 35%, var(--teal-light) 0%, var(--teal-mid) 55%, var(--teal-dark) 100%);
  }
  .card--front .card__texture { height: 268px; }
  .card--back .card__texture { height: 272px; }

  .card__name,
  .card__division,
  .card__tagline,
  .contact-row,
  .brand-mark {
    position: absolute;
    left: 0;
    width: 100%;
    text-align: center;
    font-weight: 300;
  }

  /* Front */
  .card--front .card__name { top: 122px; font-size: 52px; line-height: 1; letter-spacing: 0.5px; }
  .card--front .card__division { top: 206px; font-size: 27px; line-height: 1; letter-spacing: 1px; }
  .card__tagline { top: 289px; font-size: 20px; line-height: 1; color: var(--ink-soft); }

  .contact-row {
    top: 354px;
    display: flex;
    justify-content: space-between;
    padding: 0 60px 0 40px;
    font-size: 15px;
    color: var(--ink-soft);
    list-style: none;
  }
  .contact-row__item { display: flex; align-items: center; gap: 10px; }
  .contact-row__icon { width: 22px; height: 22px; flex: none; }

  /* Back */
  .brand-mark {
    top: 134px;
    font-size: 30px;
    line-height: 1;
    letter-spacing: 0.5px;
  }
  .card--back .card__name { top: 292px; font-size: 40px; line-height: 1; }
  .card--back .card__division { top: 350px; font-size: 19px; line-height: 1; letter-spacing: 1px; color: var(--ink-soft); }
</style>
</head>
<body>

<section class="card card--front">
  <div class="card__texture" role="img" aria-label="Dark teal lace floral pattern background"></div>
  <h1 class="card__name">Marisol Quenton</h1>
  <p class="card__division">DESIGNS</p>
  <p class="card__tagline">jewellery and object maker</p>
  <ul class="contact-row">
    <li class="contact-row__item">
      <svg class="contact-row__icon" viewBox="0 0 22 22" aria-hidden="true">
        <circle cx="11" cy="11" r="10" fill="none" stroke="#c9d3d1" stroke-width="1.2"/>
        <path d="M7.5 6.5 L9.3 6.2 L10.2 8.6 L9 9.6 Q10 11.9 12.4 13 L13.4 11.8 L15.8 12.7 L15.5 14.5 Q11.5 15.5 8.5 11.8 Q6.7 9.3 7.5 6.5 Z" fill="#c9d3d1"/>
      </svg>
      <span>047-612-5093</span>
    </li>
    <li class="contact-row__item">
      <svg class="contact-row__icon" viewBox="0 0 22 22" aria-hidden="true">
        <circle cx="11" cy="11" r="10" fill="none" stroke="#c9d3d1" stroke-width="1.2"/>
        <rect x="6" y="7.5" width="10" height="7" fill="none" stroke="#c9d3d1" stroke-width="1.1"/>
        <path d="M6 7.5 L11 11.5 L16 7.5" fill="none" stroke="#c9d3d1" stroke-width="1.1"/>
      </svg>
      <span>kmquenton4@mailvora.com</span>
    </li>
    <li class="contact-row__item">
      <svg class="contact-row__icon" viewBox="0 0 22 22" aria-hidden="true">
        <circle cx="11" cy="11" r="10" fill="none" stroke="#c9d3d1" stroke-width="1.2"/>
      </svg>
      <span>@marisolquenton</span>
    </li>
  </ul>
</section>

<section class="card card--back">
  <div class="card__texture" role="img" aria-label="Dark teal lace floral pattern background"></div>
  <p class="brand-mark">Marisol Quenton</p>
  <h2 class="card__name">Marisol Quenton</h2>
  <p class="card__division">DESIGNS</p>
</section>

</body>
</html>
```